Veltarum

Standard Business Card design.
Sample two-sided design uploaded. White front, Black back.
Would like white shield to be on all black background side.
Willing to look at a couple creative designs, but nothing crazy.
Preference for a classic, confident, strong design.

```html
<!DOCTYPE html>
<html lang="en">
<head>
<meta charset="utf-8">
<title>Veltarum – Business Card</title>
<link href="https://fonts.googleapis.com/css2?family=Arimo:wght@400;700&family=Fira+Sans:wght@600&display=swap" rel="stylesheet">
<style>
  :root {
    --ink: #1a1a1a;
    --card-dark: #1c1a1a;
    --paper: #ffffff;
    --frame: #3a3a3a;
    --card-edge: #8a8a8a;
    --icon-line: #2a2a2a;
  }
  * { margin: 0; padding: 0; box-sizing: border-box; }
  html, body { width: 1200px; height: 1200px; overflow: hidden; background: var(--paper); }
  .sheet {
    position: relative;
    width: 1200px;
    height: 1200px;
    border: 2px solid var(--frame);
    background: var(--paper);
  }
  .card {
    position: absolute;
    left: 235px;
    width: 730px;
    height: 417px;
    border-radius: 12px;
  }
  .card--back { top: 163px; background: var(--card-dark); }
  .card--front { top: 620px; background: var(--paper); border: 1.5px solid var(--card-edge); }

  .brand-name {
    position: absolute;
    left: 0; right: 0;
    top: 186px;
    text-align: center;
    font-family: "Arimo", Arial, sans-serif;
    font-weight: 700;
    font-size: 40px;
    letter-spacing: 6px;
    color: var(--paper);
  }

  .holder {
    position: absolute;
    right: 476px;
    top: 178px;
    text-align: right;
    font-family: "Arimo", Arial, sans-serif;
    color: var(--ink);
  }
  .holder__name { font-weight: 700; font-size: 26px; line-height: 30px; }
  .holder__role { font-weight: 400; font-size: 19px; line-height: 22px; }

  .divider { position: absolute; top: 110px; height: 194px; background: var(--ink); }
  .divider--thick { left: 272px; width: 3px; }
  .divider--thin { left: 278px; width: 1px; }

  .contacts {
    position: absolute;
    left: 300px;
    top: 110px;
    list-style: none;
  }
  .contact {
    display: flex;
    align-items: center;
    height: 40.5px;
    font-family: "Fira Sans", Arial, sans-serif;
    font-weight: 600;
    font-size: 19px;
    color: var(--ink);
  }
  .contact__icon { width: 32px; height: 32px; margin-right: 23px; flex: none; }
</style>
</head>
<body>
<main class="sheet">
  <section class="card card--back" aria-label="Card back">
    <div class="brand-name">VELTARUM</div>
  </section>

  <section class="card card--front" aria-label="Card front">
    <div class="holder">
      <p class="holder__name">Daniel R. Hale</p>
      <p class="holder__role">Manager</p>
    </div>
    <span class="divider divider--thick"></span>
    <span class="divider divider--thin"></span>

    <ul class="contacts">
      <li class="contact">
        <svg class="contact__icon" viewBox="0 0 32 32" fill="none" stroke="var(--icon-line)" stroke-width="1.2">
          <circle cx="16" cy="16" r="15"/>
          <rect x="12" y="8.5" width="8" height="15" rx="1.2"/>
          <line x1="15" y1="21" x2="17" y2="21"/>
        </svg>
        0812 4471 2093
      </li>
      <li class="contact">
        <svg class="contact__icon" viewBox="0 0 32 32" fill="none" stroke="var(--icon-line)" stroke-width="1.2">
          <circle cx="16" cy="16" r="15"/>
          <path d="M9 13 Q16 8 23 13 L21.5 15 L19 14 L19 12.5 Q16 11.5 13 12.5 L13 14 L10.5 15 Z"/>
          <rect x="11" y="15.5" width="10" height="7" rx="1"/>
          <circle cx="16" cy="19" r="1.6"/>
        </svg>
        070-318-2240
      </li>
      <li class="contact">
        <svg class="contact__icon" viewBox="0 0 32 32" fill="none" stroke="var(--icon-line)" stroke-width="1.2">
          <circle cx="16" cy="16" r="15"/>
          <circle cx="16" cy="16" r="7"/>
          <ellipse cx="16" cy="16" rx="3" ry="7"/>
          <line x1="9" y1="16" x2="23" y2="16"/>
        </svg>
        veltarum.com
      </li>
      <li class="contact">
        <svg class="contact__icon" viewBox="0 0 32 32" fill="none" stroke="var(--icon-line)" stroke-width="1.2">
          <circle cx="16" cy="16" r="15"/>
          <rect x="9" y="11" width="14" height="10" rx="1"/>
          <path d="M9 11.5 L16 17 L23 11.5"/>
        </svg>
        mail@veltarum.com
      </li>
      <li class="contact">
        <svg class="contact__icon" viewBox="0 0 32 32" fill="none" stroke="var(--icon-line)" stroke-width="1.2">
          <circle cx="16" cy="16" r="15"/>
          <path d="M16 24 C12 19 11 16.5 11 14 A5 5 0 0 1 21 14 C21 16.5 20 19 16 24 Z"/>
          <circle cx="16" cy="14" r="1.8"/>
        </svg>
        Kent Road, Orvale 4120
      </li>
    </ul>
  </section>
</main>
</body>
</html>
```